Security and Automation Company based in Texas and needs logo design also

Looking for a new logo design for our company - we are based in Texas and specialize in camera, security and home automation - We do want the main company name(Keystone Guard and Controls of Texas) with our parent company in small letters below (a Brindle Oak Partners, LLC Company) and our License number needs to be included in the design - K74836 - Darker shades of blue preferred

Target Market(s)

We work with everyone from home to large corporate - so clean design would be helpful

Industry/Entity Type

It Company

Contact Information for Business Card

PO Box 4862
Cedar Hollow, Texas 75917
Leave a spot for the phone number and email address

Logo Text

Keystone Guard and Controls of Texas/a Brindle Oak Partners Company/K74836

Font styles to use
Sans Serif

Colors
0255a3

```html
<!DOCTYPE html>
<html lang="en">
<head>
<meta charset="utf-8">
<title>Keystone Guard and Controls of Texas – Business Card</title>
<link rel="stylesheet" href="https://fonts.googleapis.com/css2?family=Josefin+Sans:wght@300;400&family=Montserrat:wght@600;700&family=Open+Sans:wght@400&display=swap">
<style>
  :root {
    --page: #e4e6e6;
    --navy-deep: #1d4664;
    --navy: #235a80;
    --navy-band: #1f5a7e;
    --accent: #3aa6dc;
    --accent-soft: rgba(58, 166, 220, 0.3);
    --ink: #14263a;
    --muted: #4a4f55;
    --card-white: #ffffff;
    --card-grey: #d9dadb;
  }
  html, body {
    margin: 0;
    width: 1200px;
    height: 900px;
    overflow: hidden;
    background: var(--page);
  }
  .canvas {
    position: relative;
    width: 1200px;
    height: 900px;
  }
  .card {
    position: absolute;
    width: 500px;
    height: 286px;
    overflow: hidden;
    box-shadow: 0 6px 14px rgba(0, 0, 0, 0.25);
  }

  /* Front */
  .card-front {
    left: 120px;
    top: 170px;
    background: linear-gradient(160deg, var(--navy) 0%, var(--navy-deep) 100%);
  }
  .front-texture {
    position: absolute;
    inset: 0;
    background:
      radial-gradient(ellipse at 75% 20%, rgba(80, 150, 190, 0.25), transparent 60%),
      radial-gradient(ellipse at 20% 85%, rgba(80, 150, 190, 0.18), transparent 55%);
  }
  .brand {
    position: absolute;
    left: 60px;
    top: 100px;
    display: flex;
    align-items: center;
    gap: 22px;
  }
  .brand-dot {
    width: 80px;
    height: 80px;
    border-radius: 50%;
    background: var(--accent);
    flex: none;
  }
  .brand-name {
    margin: 0;
    font-family: "Josefin Sans", sans-serif;
    font-weight: 300;
    font-size: 24px;
    line-height: 1.15;
    letter-spacing: 0.3px;
    color: var(--accent);
    width: 260px;
  }
  .brand-sub {
    margin: 7px 0 0;
    font-family: "Josefin Sans", sans-serif;
    font-weight: 300;
    font-size: 10px;
    letter-spacing: 0.4px;
    color: var(--accent);
  }

  /* Back */
  .card-back {
    left: 580px;
    top: 440px;
    background: linear-gradient(180deg, var(--card-white) 0%, var(--card-white) 45%, var(--card-grey) 100%);
  }
  .back-band {
    position: absolute;
    left: 0;
    right: 0;
    top: 104px;
    height: 68px;
    overflow: hidden;
    background: linear-gradient(90deg, var(--navy-band), var(--navy));
  }
  .band-texture {
    position: absolute;
    right: 0;
    top: 0;
    width: 140px;
    height: 100%;
    background: linear-gradient(90deg, transparent, rgba(90, 160, 200, 0.3));
  }
  .band-mark {
    position: absolute;
    left: 100px;
    top: 6px;
    width: 56px;
    height: 56px;
    border-radius: 50%;
    background: var(--accent-soft);
  }
  .person {
    position: absolute;
    left: 40px;
    top: 66px;
  }
  .person-name {
    margin: 0;
    font-family: "Montserrat", sans-serif;
    font-weight: 700;
    font-size: 18px;
    line-height: 22px;
    letter-spacing: 0.3px;
    color: var(--ink);
    text-transform: uppercase;
  }
  .person-role {
    margin: 0 0 0 44px;
    font-family: "Montserrat", sans-serif;
    font-weight: 600;
    font-size: 6.5px;
    line-height: 9px;
    letter-spacing: 0.6px;
    color: var(--navy);
    text-transform: uppercase;
  }
  .contact {
    position: absolute;
    left: 300px;
    top: 186px;
    margin: 0;
    padding: 0;
    list-style: none;
    font-family: "Open Sans", sans-serif;
    font-size: 11px;
    line-height: 13px;
    letter-spacing: 1px;
    color: var(--muted);
  }
  .contact li {
    display: flex;
    gap: 8px;
  }
  .contact svg {
    width: 8px;
    height: 8px;
    margin-top: 3px;
    flex: none;
    fill: var(--accent);
  }
  .contact .no-icon {
    padding-left: 16px;
  }
</style>
</head>
<body>
<main class="canvas">

  <section class="card card-front" aria-label="Business card front">
    <div class="front-texture" role="img" aria-label="Soft blue digital grid texture"></div>
    <div class="brand">
      <span class="brand-dot" aria-hidden="true"></span>
      <div>
        <h1 class="brand-name">Keystone Guard and Controls of Texas</h1>
        <p class="brand-sub">Brindle Oak Partners, LLC · K74836</p>
      </div>
    </div>
  </section>

  <section class="card card-back" aria-label="Business card back">
    <div class="back-band">
      <div class="band-texture" role="img" aria-label="Faint blue digital grid texture"></div>
      <span class="band-mark" aria-hidden="true"></span>
    </div>
    <div class="person">
      <p class="person-name">Dale Hartwell</p>
      <p class="person-role">General Manager</p>
    </div>
    <ul class="contact">
      <li>
        <svg viewBox="0 0 10 10" aria-hidden="true"><path d="M2 0.5 L4 2.5 L3 4 Q4.5 6 6 7 L7.5 6 L9.5 8 L8 9.5 Q3 9 0.5 2 Z"/></svg>
        <span>000 111 222</span>
      </li>
      <li>
        <svg viewBox="0 0 10 10" aria-hidden="true"><path d="M0.5 2 H9.5 V8.5 H0.5 Z M1 2.5 L5 5.5 L9 2.5" stroke="#fff" stroke-width="0.8"/></svg>
        <span>hartwell@mail.com</span>
      </li>
      <li>
        <svg viewBox="0 0 10 10" aria-hidden="true"><path d="M5 0.5 A3.2 3.2 0 0 1 8.2 3.7 C8.2 6 5 9.5 5 9.5 C5 9.5 1.8 6 1.8 3.7 A3.2 3.2 0 0 1 5 0.5 Z"/></svg>
        <span>Cedar Hollow,</span>
      </li>
      <li class="no-icon">Texas 75917</li>
      <li class="no-icon">PO Box 4862</li>
    </ul>
  </section>

</main>
</body>
</html>
```